Ardenwell Building and Property Services needs a business card design

We need a business card design for our building and property services business. We already have a logo we just need a creative design and layout on a business card. Emphasis on clean, modern, professional.
Our client targets are mainly body corporates, building managers, construction managers.
We are a building services company that lean more to structural repair of buildings, through concrete rectification and carbon fibre strengthening.
We also refurbish facades, rendering, painting etc
We target higher end body corporates in prestigious locations, hence why we'd like our cards to reflect professionalism, strength, efficiency

Target Market(s)

body corporates, building managers, construction managers

Industry/Entity Type

Construction

Contact Information for Business Card

Ardenwell is the main word, with 'Building and Property Services' underneath.
Level 17, 82 Harlow Street
MERRIDALE
Melbourne
Vic 3094
T: 9518 2736
Duncan Ferris - Director
dunardenwell@mailbox-example.com

Requirements
Must have
• Stand out on the back of the card- strong/ bold, company logo
• All of the contact details written above
Should not have
• I'd like the card to stand out, especially on the back. Id like the company logo to be prominent, although feel free to be creative around it. But remain clean and professional

```html
<!DOCTYPE html>
<html lang="en">
<head>
<meta charset="utf-8">
<title>Ardenwell Building and Property Services – Business Card</title>
<link rel="stylesheet" href="https://fonts.googleapis.com/css2?family=Cinzel:wght@400;600&family=Open+Sans:wght@400&display=swap">
<style>
  :root {
    --stage: #2b2b2d;
    --card-light: #eceef0;
    --card-light-edge: #d6d8db;
    --card-dark: #050506;
    --brand-blue: #1a8fd8;
    --brand-blue-deep: #0f6fb3;
    --ink-white: #f4f4f4;
    --ink-grey: #9a9ca0;
  }
  * { margin: 0; padding: 0; box-sizing: border-box; }
  html, body { width: 1200px; height: 879px; overflow: hidden; }
  body {
    background: var(--stage);
    position: relative;
    font-family: "Open Sans", Arial, sans-serif;
  }
  .card {
    position: absolute;
    width: 540px;
    height: 310px;
    border-radius: 3px;
    overflow: hidden;
    box-shadow: 0 14px 30px rgba(0,0,0,0.45);
  }

  /* Front */
  .card-front {
    left: 70px; top: 110px;
    background: linear-gradient(135deg, #f7f8f9 0%, var(--card-light) 55%, var(--card-light-edge) 100%);
    display: flex; flex-direction: column; align-items: center; justify-content: center;
  }
  .card-front .brand-mark {
    width: 22px; height: 22px; border-radius: 50%;
    background: var(--brand-blue);
    margin-bottom: 16px;
  }
  .card-front .brand-name {
    font-family: "Cinzel", Georgia, serif;
    font-weight: 600;
    font-size: 34px;
    letter-spacing: 3px;
    color: var(--brand-blue);
  }
  .card-front .brand-tagline {
    font-family: "Cinzel", Georgia, serif;
    font-size: 9px;
    letter-spacing: 1.6px;
    color: var(--brand-blue);
    margin-top: 4px;
  }

  /* Back */
  .card-back {
    left: 590px; top: 460px;
    background: var(--card-dark);
  }
  .card-back .brand-block {
    position: absolute; left: 34px; top: 118px;
  }
  .card-back .brand-mark {
    width: 18px; height: 18px; border-radius: 50%;
    background: var(--brand-blue);
    margin-bottom: 12px;
  }
  .card-back .brand-name {
    font-family: "Cinzel", Georgia, serif;
    font-weight: 600;
    font-size: 27px;
    letter-spacing: 2px;
    color: var(--brand-blue);
    line-height: 1;
  }
  .card-back .brand-tagline {
    font-family: "Cinzel", Georgia, serif;
    font-size: 7.5px;
    letter-spacing: 1.2px;
    color: var(--ink-white);
    margin-top: 4px;
  }
  .person {
    position: absolute; right: 34px; top: 38px; text-align: right;
  }
  .person-name {
    font-family: "Cinzel", Georgia, serif;
    font-size: 19px;
    color: var(--ink-white);
    letter-spacing: 0.5px;
  }
  .person-title {
    font-family: "Cinzel", Georgia, serif;
    font-size: 10px;
    letter-spacing: 4px;
    color: var(--ink-grey);
    margin-top: 2px;
  }
  .contact-list {
    position: absolute; right: 34px; top: 112px;
    list-style: none; text-align: right;
    font-size: 12.5px; line-height: 17px;
    color: var(--brand-blue);
  }
  .contact-list li { display: flex; justify-content: flex-end; align-items: center; gap: 7px; }
  .contact-list svg { width: 9px; height: 9px; fill: var(--brand-blue); }
  .address {
    position: absolute; left: 34px; bottom: 26px;
    font-size: 13.5px; line-height: 20px;
    color: var(--brand-blue);
  }
  .accent-stripe {
    position: absolute; right: 0; bottom: 100px;
    width: 250px; height: 12px;
  }
</style>
</head>
<body>

  <section class="card card-front" aria-label="Business card front">
    <span class="brand-mark"></span>
    <div class="brand-name">ARDENWELL</div>
    <div class="brand-tagline">BUILDING AND PROPERTY SERVICES</div>
  </section>

  <section class="card card-back" aria-label="Business card back">
    <div class="brand-block">
      <span class="brand-mark" style="display:block"></span>
      <div class="brand-name">ARDENWELL</div>
      <div class="brand-tagline">BUILDING AND PROPERTY SERVICES</div>
    </div>

    <div class="person">
      <div class="person-name">Duncan Ferris</div>
      <div class="person-title">DIRECTOR</div>
    </div>

    <ul class="contact-list">
      <li>9518 2736
        <svg viewBox="0 0 10 10"><path d="M2 0.5 L3.6 0.5 L4.2 3 L3 3.8 Q4 6 6.2 7 L7 5.8 L9.5 6.4 L9.5 8 Q9.5 9.5 8 9.5 Q1 9 0.5 2 Q0.5 0.5 2 0.5Z"/></svg>
      </li>
      <li>www.ardenwell-example.com
        <svg viewBox="0 0 10 10"><circle cx="5" cy="5" r="4.5"/></svg>
      </li>
      <li>dunardenwell@mailbox-example.com
        <svg viewBox="0 0 10 10"><rect x="0.5" y="2" width="9" height="6.5"/></svg>
      </li>
    </ul>

    <svg class="accent-stripe" viewBox="0 0 250 12" preserveAspectRatio="none" aria-hidden="true">
      <polygon points="12,0 250,0 250,12 0,12" fill="var(--brand-blue)"/>
    </svg>

    <address class="address" style="font-style:normal">
      Level 17, 82 Harlow Street<br>
      MERRIDALE&nbsp; / Melbourne / Vic 3094
    </address>
  </section>

</body>
</html>
```